Beyond The Ledger Double Sided DL Flyer

We need a double sided flyer that we provide to a Real Estate agent for leeds. It should provide our basic services as well as a modern look and feel. The brochure should incorporate our Brand colors and have a graphic that centres around money and property. I have included a couple of pictures that we like (but have not yet purchased from PIXVAULT) as an indication of the type of picture we like.

WE need to also show the Beyond The Ledger brand and have our Phone / address's and email details.

Target Market(s)

Realestate clients (Property Investors)

Industry/Entity Type

Financial Planning

Requirements
Must have
• Picture on Front (maybe the logo on back)
• Please incorporate existing logo colours.

```html
<!DOCTYPE html>
<html lang="en">
<head>
<meta charset="utf-8">
<title>Beyond The Ledger – DL Flyer</title>
<link rel="stylesheet" href="https://fonts.googleapis.com/css2?family=Oswald:wght@600&family=Lato:ital,wght@0,400;0,700;0,900;1,400&display=swap">
<style>
  :root{
    --green:#8cc63f;
    --green-deep:#5e9e2c;
    --green-light:#b6d94a;
    --charcoal:#1e1e1e;
    --ink:#222;
    --white:#fff;
    --stage:#e4e4e4;
  }
  *{box-sizing:border-box;margin:0;padding:0}
  html,body{width:1200px;height:902px;overflow:hidden}
  body{background:var(--stage);font-family:'Lato',sans-serif;position:relative}
  .flyer{position:absolute;width:367px;height:754px;overflow:hidden;box-shadow:0 6px 18px rgba(0,0,0,.35)}
  .flyer--front{left:126px;top:28px}
  .flyer--back{left:719px;top:114px}
  .flyer__art{position:absolute;inset:0;width:100%;height:100%}
  .abs{position:absolute}

  .headline{left:0;right:0;top:34px;text-align:center;font-family:'Oswald',sans-serif;font-weight:600;font-size:35px;letter-spacing:.3px;color:var(--white)}
  .headline span{color:var(--green)}

  .brand{display:flex;align-items:center;gap:7px;font-family:'Lato',sans-serif;font-weight:900;font-size:16px;color:var(--green-deep);letter-spacing:.3px;white-space:nowrap}
  .brand__dot{width:11px;height:11px;border-radius:50%;background:var(--green-deep)}
  .front-brand{left:172px;top:478px}
  .back-brand{left:0;right:0;top:48px;justify-content:center;font-size:18px}

  .services{left:173px;top:540px;width:190px}
  .services__title{font-size:8.5px;font-weight:900;color:var(--ink);line-height:1.25}
  .services__title span{color:var(--green-deep)}
  .services__list{list-style:none;margin-top:14px}
  .services__list li{font-style:italic;font-size:8.2px;color:var(--ink);line-height:15.4px;padding-left:18px;position:relative}
  .services__list li::before{content:"";position:absolute;left:0;top:5px;width:6px;height:6px;border-radius:50%;background:var(--green-deep)}

  .contact-front{left:20px;right:0;top:698px;text-align:center;color:var(--ink)}
  .phone{display:inline-flex;align-items:center;gap:5px;font-weight:700;font-size:15px}
  .phone svg{width:11px;height:11px}
  .address{font-size:8.2px;font-weight:700;line-height:11px}
  .address svg{width:7px;height:8px;vertical-align:-1px;margin-right:3px}

  .role{left:90px;width:187px;top:458px;height:26px;border-radius:6px;background:var(--green-deep);color:var(--white);font-size:11px;letter-spacing:.3px;display:flex;align-items:center;justify-content:center}
  .role::before,.role::after{content:"";position:absolute;top:10px;width:6px;height:6px;border-radius:50%;background:var(--charcoal)}
  .role::before{left:6px}.role::after{right:6px}
  .person{left:0;right:0;top:494px;text-align:center;color:var(--white);font-size:11px;font-weight:700}
  .call{left:50px;width:268px;top:540px;height:28px;border:1.5px solid var(--green);border-radius:8px;display:flex;align-items:center;justify-content:center;gap:6px;color:var(--white);font-size:15px}
  .call__label{color:var(--green);font-weight:700}
  .call svg{width:11px;height:11px}
  .contact-back{left:0;right:0;top:580px;text-align:center;color:var(--white)}
  .contact-back .address{font-size:8.8px}
  .email{margin-top:10px;font-size:9px;font-weight:700}
  .email svg{width:8px;height:6px;margin-right:6px;vertical-align:0}
  .follow{left:0;right:0;top:652px;display:flex;justify-content:center;align-items:center;gap:4px;font-size:9px;font-weight:700;color:var(--green)}
  .follow__label{margin-right:6px}
  .follow__chip{width:15px;height:15px;border-radius:2px;background:#4a8fd0}
  .follow__chip:first-of-type{background:#d44b3a}
  .website{left:0;right:0;top:720px;text-align:center;font-size:10px;font-weight:900;letter-spacing:1.4px;color:var(--charcoal)}
</style>
</head>
<body>

<section class="flyer flyer--front">
  <svg class="flyer__art" viewBox="0 0 367 754" aria-hidden="true">
    <defs>
      <linearGradient id="darkTop" x1="0" y1="0" x2="1" y2="1">
        <stop offset="0" stop-color="#1a1a1a"/><stop offset="1" stop-color="#3b3b3b"/>
      </linearGradient>
      <linearGradient id="gardenTone" x1="0" y1="0" x2="0.35" y2="1">
        <stop offset="0" stop-color="#2f5e22"/><stop offset=".35" stop-color="#5a8f3a"/><stop offset=".62" stop-color="#7fae55"/><stop offset=".8" stop-color="#8f8a72"/><stop offset="1" stop-color="#6e5640"/>
      </linearGradient>
      <linearGradient id="jarTone" x1="0" y1="0" x2="1" y2="0.4">
        <stop offset="0" stop-color="#8fae5e"/><stop offset=".45" stop-color="#b9ab86"/><stop offset=".75" stop-color="#e3dcc9" stop-opacity=".8"/><stop offset="1" stop-color="#fff" stop-opacity="0"/>
      </linearGradient>
      <linearGradient id="bandGreen" x1="0" y1="0" x2="1" y2="0">
        <stop offset="0" stop-color="var(--green-deep)"/><stop offset="1" stop-color="var(--green-light)"/>
      </linearGradient>
    </defs>
    <rect width="367" height="754" fill="#fff"/>
    <rect width="367" height="260" fill="url(#darkTop)"/>
    <path d="M0,176 C130,146 290,126 367,80 L367,754 L0,754Z" fill="#fff"/>
    <path d="M0,184 C130,154 290,134 367,88" fill="none" stroke="var(--green)" stroke-width="5"/>
    <path d="M0,196 C130,166 300,146 367,104 L367,300 C320,392 180,420 0,400Z" fill="url(#gardenTone)" role="img" aria-label="Photo: hand watering a seedling growing from a coin jar beside coin stacks and a small house figure"/>
    <path d="M0,404 C180,426 330,398 367,310" fill="none" stroke="var(--green)" stroke-width="5"/>
    <path d="M0,414 C185,438 335,408 367,326" fill="none" stroke="var(--charcoal)" stroke-width="5"/>
    <rect x="0" y="450" width="180" height="230" fill="url(#jarTone)" role="img" aria-label="Photo: seedling sprouting from a glass jar of coins"/>
    <path d="M0,686 C120,664 260,664 367,676" fill="none" stroke="var(--charcoal)" stroke-width="5"/>
    <path d="M0,692 C120,672 260,672 367,684 L367,754 L0,754Z" fill="url(#bandGreen)"/>
  </svg>

  <h1 class="abs headline">BEYOND THE <span>LEDGER</span></h1>

  <div class="abs brand front-brand"><span class="brand__dot"></span>Beyond The Ledger</div>

  <div class="abs services">
    <p class="services__title">ACCOUNTANTS AND FINANCIAL ADVISORS<br><span>WHO SPECIALISE IN:</span></p>
    <ul class="services__list">
      <li>Negative Gearing &amp; Investment Properties</li>
      <li>Property &amp; Capital Gains Tax Minimisation</li>
      <li>Self-Managed Superannuation Funds (SMSF)</li>
      <li>Small Business &amp; Personal Taxation</li>
      <li>Investment Advice &amp; Risk Insurances</li>
    </ul>
  </div>

  <div class="abs contact-front">
    <div class="phone">
      <svg viewBox="0 0 24 24"><circle cx="12" cy="12" r="11" fill="none" stroke="currentColor" stroke-width="2"/><path d="M8 6l2 3-1.5 1.5a8 8 0 004 4L14 13l3 2-1.5 2.5C11 17 7 13 6.5 8.5z" fill="currentColor"/></svg>
      (02) 4100 2750
    </div>
    <p class="address"><svg viewBox="0 0 10 12"><path d="M5 0a4 4 0 014 4c0 3-4 8-4 8S1 7 1 4a4 4 0 014-4z" fill="var(--white)"/></svg>7 / 118 Harbour View Rd Kenwick NSW 2251</p>
    <p class="address">2 / 39 Marlow St Baybrook NSW 2264 (By Appointment)</p>
  </div>
</section>

<section class="flyer flyer--back">
  <svg class="flyer__art" viewBox="0 0 367 754" aria-hidden="true">
    <defs>
      <linearGradient id="darkBack" x1="0" y1="0" x2="0" y2="1">
        <stop offset="0" stop-color="#2c2c2c"/><stop offset="1" stop-color="#121212"/>
      </linearGradient>
      <linearGradient id="houseTone" x1="0" y1="0" x2="1" y2="1">
        <stop offset="0" stop-color="#b9a394"/><stop offset=".3" stop-color="#e9e3dc"/><stop offset=".55" stop-color="#d7c6b8"/><stop offset=".75" stop-color="#9fc46a"/><stop offset="1" stop-color="#7f8ea0"/>
      </linearGradient>
      <linearGradient id="bandGreenBack" x1="0" y1="0" x2="1" y2="0">
        <stop offset="0" stop-color="var(--green-light)"/><stop offset="1" stop-color="var(--green-deep)"/>
      </linearGradient>
    </defs>
    <rect width="367" height="754" fill="url(#darkBack)"/>
    <path d="M0,0 H367 V175 C300,120 150,80 0,78Z" fill="#fff"/>
    <path d="M0,82 C150,86 300,125 367,178" fill="none" stroke="var(--charcoal)" stroke-width="6"/>
    <path d="M0,92 C150,96 300,135 367,188" fill="none" stroke="var(--green)" stroke-width="5"/>
    <path d="M0,100 C150,104 300,143 367,196 L367,395 C300,440 150,440 0,380Z" fill="url(#houseTone)" role="img" aria-label="Photo: hands holding a small wooden house behind coin stacks with seedlings"/>
    <path d="M0,388 C150,446 300,446 367,403" fill="none" stroke="var(--green)" stroke-width="6"/>
    <path d="M0,397 C150,455 300,455 367,412" fill="none" stroke="#fff" stroke-width="3"/>
    <path d="M0,696 C120,676 260,674 367,686" fill="none" stroke="#fff" stroke-width="8"/>
    <path d="M0,706 C120,688 260,686 367,698 L367,754 L0,754Z" fill="url(#bandGreenBack)"/>
  </svg>

  <div class="abs brand back-brand"><span class="brand__dot"></span>Beyond The Ledger</div>

  <div class="abs role">ADVISOR / ACCOUNTANT</div>
  <p class="abs person">DANIEL HARROW</p>

  <div class="abs call">
    <span class="call__label">Call Us Today :</span>
    <svg viewBox="0 0 24 24"><circle cx="12" cy="12" r="11" fill="none" stroke="currentColor" stroke-width="2"/><path d="M8 6l2 3-1.5 1.5a8 8 0 004 4L14 13l3 2-1.5 2.5C11 17 7 13 6.5 8.5z" fill="currentColor"/></svg>
    (02) 4100 2750
  </div>

  <div class="abs contact-back">
    <p class="address"><svg viewBox="0 0 10 12"><path d="M5 0a4 4 0 014 4c0 3-4 8-4 8S1 7 1 4a4 4 0 014-4z" fill="var(--green)"/></svg>7 / 118 Harbour View Rd Kenwick NSW 2251</p>
    <p class="address">2 / 39 Marlow St Baybrook NSW 2264 (By Appointment)</p>
    <p class="email"><svg viewBox="0 0 8 6"><rect width="8" height="6" fill="var(--green)"/><path d="M0 0l4 3 4-3" fill="none" stroke="#222" stroke-width=".8"/></svg>info@beyondledger.com.au</p>
  </div>

  <div class="abs follow">
    <span class="follow__label">Follow Us On :</span>
    <span class="follow__chip"></span><span class="follow__chip"></span><span class="follow__chip"></span><span class="follow__chip"></span><span class="follow__chip"></span>
  </div>

  <p class="abs website">www.beyondledger.com.au</p>
</section>

</body>
</html>
```